Web Design Project

kestrel ridge works & services needs a new web design to go with its new logo design

we provide services such as instillation of fire sprinklers, fire hydrants , fire hose reels as well as fire extinguishers and fire blankets.

we can service these as well and also do the preventitave maintaince of these too.

we can do flow testing of sprinklers,hydrants & hosereels and test back flow prevention devices as well

old page is krws.com.au

```html
<!DOCTYPE html>
<html lang="en">
<head>
<meta charset="utf-8">
<title>Kestrel Ridge Works &amp; Services</title>
<link href="https://fonts.googleapis.com/css2?family=Open+Sans:wght@400;600;700&family=Arimo:wght@400;700&display=swap" rel="stylesheet">
<style>
  :root{
    --header-red:#7a0a0d;
    --header-red-dark:#6a080b;
    --nav-orange:#f7a531;
    --nav-orange-light:#fdd58a;
    --nav-active:#a8282c;
    --page-bg:#f3f5f9;
    --panel-top:#ffffff;
    --panel-bottom:#d4d4d4;
    --footer-grey:#c4c4c4;
    --footer-bar:#a9a9a9;
    --ink:#111111;
    --rule:#444444;
    --white:#ffffff;
  }
  *{margin:0;padding:0;box-sizing:border-box}
  html,body{width:1072px;height:1200px;overflow:hidden}
  body{background:var(--page-bg);position:relative;font-family:'Arimo',Arial,sans-serif;color:var(--ink)}
  .site-header{position:absolute;left:0;top:0;width:1072px;height:148px;background:linear-gradient(var(--header-red),var(--header-red-dark))}
  .brand{position:absolute;left:118px;top:58px;display:flex;align-items:center;gap:12px;font-family:'Open Sans',sans-serif;font-weight:700;font-size:46px;line-height:1;color:#c8363a;letter-spacing:2px}
  .brand-mark{width:30px;height:30px;background:#c8363a}
  .call-now{position:absolute;left:727px;top:24px;font-family:'Open Sans',sans-serif;color:var(--white);font-size:14px;font-weight:600}
  .call-now strong{font-size:19px}
  .main-nav{position:absolute;left:0;top:154px;width:1072px;height:42px;background:linear-gradient(var(--nav-orange-light),var(--nav-orange) 45%,#f39a1e);border-top:2px solid #fff;box-shadow:0 1px 0 #e0e0e0}
  .main-nav ul{list-style:none;display:flex;position:absolute;left:118px;top:0;height:40px}
  .main-nav li{height:40px;line-height:38px;padding:0 16px;font-family:'Open Sans',sans-serif;font-size:14px;color:var(--white);text-shadow:0 1px 1px rgba(0,0,0,.35);border-right:1px solid rgba(255,255,255,.35)}
  .main-nav li.active{background:var(--nav-active);font-size:15px}
  .hero{position:absolute;left:0;top:203px;width:1072px;height:335px;background:radial-gradient(ellipse at 30% 40%,#f7a540,#e6561a 55%,#a8270c)}
  .tagline{position:absolute;left:185px;top:125px;width:505px;height:85px;background:rgba(90,20,10,.35);display:flex;align-items:center;justify-content:center;font-family:'Open Sans',sans-serif;font-size:28px;color:var(--white);text-shadow:0 2px 3px rgba(0,0,0,.5)}
  .hero-person{position:absolute;left:705px;top:85px;width:367px;height:453px;background:linear-gradient(160deg,#b58a3a,#6a5034 55%,#3b3127);border-radius:120px 120px 0 0}
  .content-panel{position:absolute;left:118px;top:538px;width:835px;height:645px;background:linear-gradient(var(--panel-top),#e8e8e8 60%,var(--panel-bottom));box-shadow:0 0 4px rgba(0,0,0,.3)}
  .service{position:absolute;top:24px;width:259px;height:370px}
  .service-photo{height:224px;border:2px solid #fff;border-radius:6px;box-shadow:0 0 2px rgba(0,0,0,.5);position:relative;overflow:hidden}
  .service-photo span{position:absolute;left:0;right:0;bottom:0;height:48px;background:rgba(255,255,255,.55);font-family:'Open Sans',sans-serif;font-size:19px;color:#111;text-align:center;line-height:50px}
  .service p{margin:20px 10px 0 10px;font-size:10.3px;line-height:12.3px;color:var(--ink)}
  .read-more{display:block;text-align:right;margin:12px 14px 0 0;font-size:10.5px;font-weight:700}
  .service + .service{border-left:1px solid #d0d0d0}
  .footer-links{position:absolute;left:0;top:442px;width:835px;height:166px;background:var(--footer-grey)}
  .link-col{position:absolute;top:14px;width:124px}
  .link-col h3{font-family:'Open Sans',sans-serif;font-weight:400;font-size:16px;padding-bottom:4px;border-bottom:1px solid var(--rule)}
  .link-col ul{list-style:none}
  .link-col li{font-size:11px;font-family:'Open Sans',sans-serif;height:22px;line-height:21px;border-bottom:1px solid var(--rule);padding-left:4px}
  .link-col li:last-child{border-bottom:none}
  .link-col li::before{content:"•";margin-right:6px}
  .col-divider{position:absolute;top:22px;width:1px;height:130px;background:#b0b0b0}
  .blog{position:absolute;left:570px;top:20px;width:250px;height:140px}
  .blog h4{font-family:'Open Sans',sans-serif;font-size:12px;font-weight:600;margin-bottom:4px}
  .blog-entry{display:flex;gap:6px;margin-bottom:12px}
  .blog-thumb{width:50px;height:46px;border:2px solid #fff;flex:none}
  .blog-entry p{font-size:10px;line-height:12px;margin-top:8px}
  .blog .read-more{position:absolute;right:10px;top:124px;margin:0;line-height:13px}
  .copyright{position:absolute;left:0;top:608px;width:835px;height:37px;background:var(--footer-bar);font-size:10.5px;text-align:center;line-height:37px}
</style>
</head>
<body>
  <header class="site-header">
    <div class="brand"><span class="brand-mark"></span>KRWS</div>
    <div class="call-now">Call Now : <strong>0042 0611 274</strong></div>
  </header>

  <nav class="main-nav">
    <ul>
      <li class="active">Home</li>
      <li>Our Service</li>
      <li>Testing</li>
      <li>Products</li>
      <li>FAQ'S</li>
      <li>About us</li>
    </ul>
  </nav>

  <section class="hero">
    <div role="img" aria-label="Wall of orange flames" style="position:absolute;inset:0"></div>
    <div class="tagline">“ Your best defence against fire ”</div>
  </section>
  <div class="hero-person" role="img" aria-label="Firefighter in helmet and turnout gear"></div>

  <main class="content-panel">
    <article class="service" style="left:18px">
      <div class="service-photo" role="img" aria-label="Fire hydrant on a wet night street" style="background:linear-gradient(160deg,#4a4a55,#8a8a96 50%,#2a2a30)"><span>Fire hydrants</span></div>
      <p>At kestrel ridge we believe that no matter how large or small your business is we can help you with the design, installation and the maintenance of your system to the standard which it was designed to. Kestrel Ridge can also supply quotations for any alterations to your Sprinklers,Hydrants &amp; Hose reel systems along with your fire detection and emergency lighting.</p>
      <span class="read-more">Read More</span>
    </article>
    <article class="service" style="left:290px">
      <div class="service-photo" role="img" aria-label="Worker on a radio behind a red fire hose reel" style="background:radial-gradient(circle at 50% 45%,#e8d8d0,#c23a42 55%,#8a1a22)"><span>Fire hose reels</span></div>
      <p>At kestrel ridge we believe that no matter how large or small your business is we can help you with the design, installation and the maintenance of your system to the standard which it was designed to. Kestrel Ridge can also supply quotations for any alterations to your Sprinklers,Hydrants &amp; Hose reel systems along with your fire detection and emergency lighting.</p>
      <span class="read-more">Read More</span>
    </article>
    <article class="service" style="left:561px">
      <div class="service-photo" role="img" aria-label="Red fire extinguisher spraying" style="background:linear-gradient(110deg,#6d8098,#c6ced8 55%,#b23030)"><span>Fire extinguishers</span></div>
      <p>At kestrel ridge we believe that no matter how large or small your business is we can help you with the design, installation and the maintenance of your system to the standard which it was designed to. Kestrel Ridge can also supply quotations for any alterations to your Sprinklers,Hydrants &amp; Hose reel systems along with your fire detection and emergency lighting.</p>
      <span class="read-more">Read More</span>
    </article>

    <footer class="footer-links">
      <div class="link-col" style="left:30px">
        <h3>Home</h3>
        <ul><li>Home</li><li>About Us</li><li>Portfolio</li><li>Our Services</li><li>Contact Us</li></ul>
      </div>
      <div class="col-divider" style="left:187px"></div>
      <div class="link-col" style="left:216px">
        <h3>Our Services</h3>
        <ul><li>Home</li><li>About Us</li><li>Portfolio</li><li>Our Services</li><li>Contact Us</li></ul>
      </div>
      <div class="col-divider" style="left:374px"></div>
      <div class="link-col" style="left:409px">
        <h3>About Us</h3>
        <ul><li>Home</li><li>About Us</li><li>Portfolio</li><li>Our Services</li><li>Contact Us</li></ul>
      </div>
      <div class="blog">
        <h4>Our Blog</h4>
        <div class="blog-entry">
          <div class="blog-thumb" role="img" aria-label="Blog author portrait" style="background:linear-gradient(#b8a060,#6a7a3a)"></div>
          <p>Lorem Ipsum is simply dummy text of the printing and typesetting industry.</p>
        </div>
        <div class="blog-entry">
          <div class="blog-thumb" role="img" aria-label="Blog author portrait" style="background:linear-gradient(#888,#2a2a2a)"></div>
          <p>Lorem Ipsum is simply dummy text of the printing and typesetting industry.</p>
        </div>
        <span class="read-more">Read More</span>
      </div>
    </footer>
    <div class="copyright">Copyright 2010 KRWS.COM.AU All Rights Reserved</div>
  </main>
</body>
</html>
```